Mango Grove Indian Restaurants 2019 Menu

Hi,
Please find attached menu text in pdf format. It contains 4 pages. Please work on the menu pages. I will further work with the winner to add the cover page and images as an extended project

Please visit www.mangogroveeats.com.au for more information

```html
<!DOCTYPE html>
<html lang="en">
<head>
<meta charset="utf-8">
<title>Mango Grove Indian Restaurants – Menu Spread</title>
<link href="https://fonts.googleapis.com/css2?family=Montserrat:wght@400;600;700&family=Noto+Serif:wght@400;700&family=Great+Vibes&display=swap" rel="stylesheet">
<style>
:root{
  --backdrop:#b5844a;
  --page:#1e1e1e;
  --page-edge:#161616;
  --gold:#e3a92f;
  --gold-soft:#c9962e;
  --ink:#f1ece4;
  --ink-dim:#bdb6ab;
  --brand-red:#c8231e;
  --white:#ffffff;
}
*{box-sizing:border-box;margin:0;padding:0}
html,body{width:1200px;height:759px;overflow:hidden}
body{background:var(--backdrop);font-family:"Montserrat",sans-serif;color:var(--ink);position:relative}
.spread{position:absolute;left:40px;top:24px;width:1120px;height:711px;display:flex;box-shadow:0 8px 24px rgba(0,0,0,.35)}
.page{position:relative;width:560px;height:711px;background:var(--page);overflow:hidden}
.page--left{border-right:1px solid var(--page-edge)}
.abs{position:absolute}
.item{position:absolute;font-size:8.5px;line-height:1.35;color:var(--ink-dim)}
.item__head{display:flex;align-items:center;gap:8px;margin-bottom:4px}
.tag{background:var(--gold);color:#1b1b1b;font-weight:700;font-size:7.5px;text-transform:uppercase;padding:3px 10px;letter-spacing:.3px}
.item__meta{font-family:"Noto Serif",serif;font-weight:700;font-size:10.5px;color:var(--ink)}
.item__desc{margin-bottom:4px}
.price-row{display:flex;gap:8px}
.price-row .name{width:108px}
.price{color:var(--gold);font-weight:600;width:30px}
.starters-title{font-family:"Great Vibes",cursive;font-size:30px;color:#1b1b1b;background:var(--gold-soft);padding:0 18px;border-radius:3px;line-height:1.2}
.price-badge{display:inline-block;background:var(--gold);color:#1b1b1b;font-weight:700;font-size:8px;padding:1px 5px;border-radius:2px}
.photo{position:absolute;border-radius:4px}
.brand{position:absolute;font-family:"Noto Serif",serif;font-weight:700;color:var(--white);background:var(--brand-red);text-align:center}
.open-box{position:absolute;left:290px;top:62px;width:168px;height:78px;background:var(--page);border:1px solid #3a3a3a;display:flex}
.open-box__time{width:74px;background:var(--white);color:var(--gold);font-family:"Noto Serif",serif;font-weight:700;text-align:center;padding-top:10px;font-size:12px;line-height:1.05}
.open-box__time b{font-size:28px;display:block}
.open-box__info{padding:8px 6px;font-size:6.5px;color:var(--ink-dim);line-height:1.6}
.open-box__info .brand{position:static;font-size:8px;padding:2px 4px;margin-bottom:4px}
.platters-title{position:absolute;left:300px;top:148px;font-family:"Noto Serif",serif;color:var(--gold);font-size:13px}
.platters-title small{display:block;font-family:"Montserrat",sans-serif;font-size:8px;color:var(--ink-dim)}
.platter-price{position:absolute;left:446px;top:146px;background:var(--gold);color:#1b1b1b;font-family:"Noto Serif",serif;font-weight:700;font-size:14px;padding:2px 10px}
.platter{position:absolute;width:210px;font-size:8px;line-height:1.35;color:var(--ink-dim)}
.platter .tag{display:inline-block;margin-bottom:3px}
.platter em{color:var(--gold);font-style:normal}
.curry-list{position:absolute;left:32px;top:278px;font-family:"Noto Serif",serif;font-size:10.5px;line-height:1.9}
.curry-list li{list-style:none;display:flex;justify-content:space-between;width:150px}
.curry-list .price-badge{font-family:"Montserrat",sans-serif;font-size:7px}
.dish{position:absolute;width:300px;font-size:8px;line-height:1.35;color:var(--ink-dim)}
.dish__name{font-family:"Noto Serif",serif;font-size:11.5px;color:var(--gold)}
.dish__name small{font-family:"Montserrat",sans-serif;font-size:7px;color:var(--ink);font-weight:600}
</style>
</head>
<body>
<main class="spread">

  <section class="page page--left">

    <article class="item" style="left:28px;top:34px;width:260px">
      <div class="item__head"><span class="tag">Chilli Dry</span><span class="item__meta">(8 pcs) DF,GF, NF hot</span></div>
      <p class="item__desc">Battered and fried vegetables/meats/seafood smothered in home-made sauce made with chilli.</p>
      <div class="price-row"><span class="name">Gobi (Cauliflower)</span><span class="price">$12</span><span>Extra per piece $1.5</span></div>
      <div class="price-row"><span class="name">Mushroom/Paneer (cheese) /Chicken</span><span class="price">$12</span><span>Extra per piece $1.5</span></div>
      <div class="price-row"><span class="name">Fish/Prawn</span><span class="price">$20</span><span>Extra per piece $1.5</span></div>
    </article>

    <article class="item" style="left:28px;top:130px;width:260px">
      <div class="item__head"><span class="tag">Manchurian Dry</span><span class="item__meta">(8 pcs) DF,GF, NF hot</span></div>
      <p class="item__desc">Battered and fried vegetables/meats/seafood that are tossed in home-made sauce made with celery, cabbage.</p>
      <div class="price-row"><span class="name">Gobi (Cauliflower)</span><span class="price">$12</span><span>Extra per piece $1.5</span></div>
      <div class="price-row"><span class="name">Mushroom/Paneer (cheese) /Chicken</span><span class="price">$14</span><span>Extra per piece $1.5</span></div>
      <div class="price-row"><span class="name">Fish/Prawn</span><span class="price">$20</span><span>Extra per piece $2.5</span></div>
    </article>

    <article class="item" style="left:28px;top:226px;width:168px">
      <div class="item__head"><span class="tag">Potato Fries</span><span class="item__meta">DF,GF, NF</span></div>
      <p class="item__desc">Thin cut straight deep fried local potatoes.</p>
      <div class="price-row"><span style="width:60px">Small</span><span class="price">$5</span></div>
      <div class="price-row"><span style="width:60px">Large</span><span class="price">$8</span></div>
    </article>

    <div class="photo" role="img" aria-label="Photo of skewered starters and a plated dish" style="left:206px;top:246px;width:78px;height:72px;background:linear-gradient(135deg,#d9a15a,#8a5a2a);transform:rotate(-6deg)"></div>

    <div class="abs" style="left:40px;top:300px"><span class="starters-title">Starters</span></div>

    <article class="item" style="left:28px;top:348px;width:260px">
      <div class="item__head"><span class="item__meta">65 (8 pcs) DF, GF, NF moderate</span></div>
      <p class="item__desc">Boneless Chicken or Gobi (cauliflower) pieces marinated in a home-made special masala mix and deep fried in spicy batter.</p>
      <div class="price-row" style="color:var(--gold)"><span style="width:110px">Gobi (Cauliflower)</span><span class="price-badge">$8</span><span style="width:50px;margin-left:20px">Chicken</span><span class="price-badge">$14</span></div>
      <div class="price-row" style="color:var(--gold);margin-top:4px"><span style="width:110px">Extra per piece Gobi</span><span class="price-badge">$1</span><span style="width:50px;margin-left:20px">Chicken</span><span class="price-badge">$1.5</span></div>
    </article>

    <article class="item" style="left:300px;top:78px;width:240px">
      <div class="item__head"><span class="tag">Onion Bhaji</span><span class="item__meta">DF,GF, NF moderate</span></div>
      <p class="item__desc">Deep fried onions marinated in chickpea, rice and corn flour with exotic spices.</p>
      <div class="price-row"><span style="width:80px">Small (5 pcs)</span><span class="price">$6</span></div>
      <div class="price-row"><span style="width:80px">Large (10 pcs)</span><span class="price">$10</span><span>Extra per piece $1</span></div>
    </article>

    <article class="item" style="left:300px;top:160px;width:240px">
      <div class="item__head"><span class="tag">Pakora</span><span class="item__meta">(8pcs) DF,GF, NF mild</span></div>
      <p class="item__desc">Deep fried pieces dipped in a mildly spiced chickpea &amp; corn flour batter mix.</p>
      <div class="price-row"><span style="width:104px">Extra per piece</span><span class="price">$0.50</span></div>
      <div class="price-row"><span style="width:104px">Fish/Prawn</span><span class="price">$20</span><span>Extra per piece $2.5</span></div>
      <div class="price-row"><span style="width:104px">Paneer (cheese) /Chicken</span><span class="price">$14</span><span>Extra per piece $1.5</span></div>
    </article>

    <article class="item" style="left:300px;top:256px;width:240px">
      <div class="item__head"><span class="tag">Palak Pakora</span><span class="item__meta">Chat (8pcs) DF,GF, NF mild</span></div>
      <p class="item__desc">Crispy fried spinach leaves dipped in mildly spiced chickpea batter, chickpea noodle <span class="price">$12</span></p>
      <div class="price-row"><span style="width:120px"></span><span>Extra per piece $1.5</span></div>
    </article>

    <div class="brand" style="left:318px;top:330px;width:140px;font-size:14px;padding:5px 0">Mango Grove</div>

    <div class="photo" role="img" aria-label="Illustrated mascot with hand-lettered slogan best taste" style="left:296px;top:368px;width:200px;height:98px;background:radial-gradient(circle at 40% 50%,#3a3a3a,#1e1e1e 70%)"></div>

    <div class="photo" role="img" aria-label="Photo collage of burgers, rice dish, pizza, salad and a takeaway bag" style="left:0;top:470px;width:420px;height:241px;border-radius:0;background:linear-gradient(160deg,#6b4a2e 0%,#c98b45 40%,#e6c08a 60%,#5a3c22 100%)"></div>
  </section>

  <section class="page page--right">

    <div class="photo" role="img" aria-label="Photo of fried chicken with noodles and vegetables" style="left:30px;top:26px;width:210px;height:112px;background:linear-gradient(135deg,#e8e2d6,#c98a45 45%,#6f9a3a 80%)"></div>

    <div class="open-box">
      <div class="open-box__time">OPEN<b>11</b>AM</div>
      <div class="open-box__info">
        <div class="brand">Mango Grove</div>
        <div>Ph: 08 9000 1234</div>
        <div>www.mangogroveeats.com.au</div>
      </div>
    </div>

    <div class="platters-title">Entrée Platters<small>for one person</small></div>
    <div class="platter-price">$10</div>

    <div class="platter" style="left:28px;top:178px"><span class="tag">Chicken Platter</span><br><em>One piece of each :</em> chicken 65, lemon chicken tikka, tandoori chicken on bone and chicken samosa</div>
    <div class="platter" style="left:28px;top:222px"><span class="tag">Mixed Platter</span><br><em>2 pieces of each :</em> onion bhaji, Chicken 65, Lemon chicken tikka, and Gobi 65</div>
    <div class="platter" style="left:290px;top:190px;width:240px"><span class="tag">Tandoori Platter</span><br><em>One piece of each :</em> lemon chicken tikka, tandoori chicken on bone, Seekh kebab and paneer (cheese)</div>
    <div class="platter" style="left:290px;top:236px;width:240px"><span class="tag">Vegan Platter</span><br><em>3 pieces of each :</em> onion bhaji, mixed pakoras and tossed veggies</div>

    <ul class="curry-list">
      <li><span>CURRIES Veg</span><span class="price-badge">$16</span></li>
      <li><span>Paneer (Cheese)</span><span class="price-badge">$18</span></li>
      <li><span>Chicken</span><span class="price-badge">$22</span></li>
      <li><span>Lamb</span><span class="price-badge">$24</span></li>
      <li><span>Seafood</span><span class="price-badge">$25</span></li>
    </ul>

    <div class="dish" style="left:216px;top:286px"><div class="dish__name">Aam (Mango) Chicken <small>GF mild</small></div>Boneless chicken pieces are cooked with exotic spices, ginger and garlic and then simmered in a semi thick sauce made with onion base, nut paste, kewra.</div>
    <div class="dish" style="left:216px;top:336px"><div class="dish__name">Aloo Khatte Meethe <small>GF, DF, NF mild</small></div>Cubes of boiled and fried potato stir-fried with tamarind and date sauce made from young ginger, green chillies and a few exotic spices.</div>
    <div class="dish" style="left:196px;top:388px;width:230px"><div class="dish__name">Aloo Gobi Adraki <small>GF, DF option, NF medium, hot</small></div>Deep fried cauliflower and potatoes cooked in a thick onion tomato masala with butter, garlic and a few exotic spices.</div>
    <div class="dish" style="left:196px;top:446px;width:230px"><div class="dish__name">Aloo Chutney Wale <small>GF, NF moderate</small></div>Cubes of boiled and fried potatos stir-fried with mint coriander sauce made with yoghurt, young ginger, green chillies.</div>
    <div class="dish" style="left:196px;top:500px;width:310px"><div class="dish__name">Aloo Gosht (Potato with lamb) <small>GF moderate</small></div>Diced lamb pieces are cooked with exotic spices, ginger and garlic and then simmered along with boiled potato in a thin sauce made with onion base, home-made special spice masala mix, mint, coriander, cashew nut paste.</div>
    <div class="dish" style="left:196px;top:570px;width:200px"><div class="dish__name">Aloo Jeera <small>GF, DF option, NF moderate</small></div>Boiled potatoes tossed in butter with simple masalas, toasted cumin seeds, chopped ginger garlic coriander.</div>

    <div class="photo" role="img" aria-label="Illustration of a chef holding a spatula and cleaver" style="left:20px;top:420px;width:170px;height:291px;background:linear-gradient(180deg,#3a3a3a,#bdbdbd 50%,#2a2a2a)"></div>
    <div class="photo" role="img" aria-label="Photo of aloo gobi in a copper bowl" style="left:436px;top:390px;width:110px;height:80px;border-radius:50%;background:radial-gradient(circle,#e0a33c,#8a5a22 75%)"></div>
    <div class="photo" role="img" aria-label="Photo of a creamy yellow curry in a white bowl" style="left:404px;top:600px;width:150px;height:90px;background:radial-gradient(ellipse,#e7a233 40%,#f2efe9 70%)"></div>
  </section>
</main>
</body>
</html>
```